Reskinning of an eSport related app

We're looking for a redesign of an esport related community app. It should look very sharp and modern like trending fitness apps. Logo and general CI is done and fixed. UI needs to be reworked. In detail: - Overall GUI and Look and Feel - Playercard, Friends List, Achievement List - Icons for Achievements - Status system (Actually done via special borders) - Torvu Logo and dragon head are fixed, it can not be changed Actual Designs attached and so styles and look and feel we like. What we dont like very much at our actual design: - Look and feel of the borders. They need to look better and more modern. It is a break of the style - The look needs to be fresh, like fitness with asiatic touch - Good achievement icons are needed. Personal tryout link of the actual version: (It will mainly be used on mobile.) Https: //zq7arena.plomb. site / quick gear / people / 3a2d71c0-5b1e-4e2f-9c3a-7d8e0f1b2c44

```html
<!DOCTYPE html>
<html lang="en">
<head>
<meta charset="utf-8">
<title>Torvu – App Screens</title>
<link href="https://fonts.googleapis.com/css2?family=Open+Sans:wght@400;600;700&display=swap" rel="stylesheet">
<style>
  :root {
    --page-bg-top: #0a1d28;
    --page-bg-mid: #0f3346;
    --page-bg-low: #06161f;
    --screen-top: #2b5369;
    --screen-bottom: #3c6b83;
    --screen-bar: #20394a;
    --card-bg: rgba(255,255,255,0.07);
    --card-line: rgba(255,255,255,0.28);
    --text: #ffffff;
    --text-soft: #c9dbe5;
    --text-dim: #9fbccb;
    --accent: #19c3f0;
    --brand-ink: #0f2231;
    --gold: #f6c623;
    --silver: #dfe4e8;
    --bronze: #d9852f;
    --rare: #f0883a;
    --epic: #f4c21f;
    --button-bg: #112a38;
    --icon-bg: #173346;
  }
  * { box-sizing: border-box; margin: 0; padding: 0; }
  html, body { width: 1200px; height: 660px; overflow: hidden; }
  body {
    font-family: "Open Sans", Arial, sans-serif;
    color: var(--text);
    background: linear-gradient(180deg, var(--page-bg-top) 0%, var(--page-bg-mid) 45%, var(--page-bg-low) 100%);
    position: relative;
  }
  .screen {
    position: absolute; top: 117px; width: 202px; height: 438px; overflow: hidden;
    background: linear-gradient(180deg, var(--screen-top), var(--screen-bottom));
  }
  .screen__bar { height: 17px; background: var(--screen-bar); }
  .screen__backdrop {
    position: absolute; inset: 17px 0 0 0;
    background: radial-gradient(ellipse at 70% 60%, rgba(120,160,180,0.28), transparent 60%),
                linear-gradient(180deg, #2b5369, #365f76 60%, #2f5a72);
  }
  .header { position: absolute; top: 26px; left: 13px; right: 12px; height: 42px; display: flex; align-items: center; }
  .brand { display: flex; align-items: center; gap: 6px; }
  .brand__mark { width: 22px; height: 22px; border-radius: 50%; background: var(--brand-ink); }
  .brand__name { font-size: 17px; font-weight: 600; color: var(--brand-ink); letter-spacing: 0.5px; }
  .header__login { margin-left: auto; font-size: 8.5px; color: var(--accent); margin-right: 7px; }
  .header__login--bold { font-weight: 600; font-size: 9px; }
  .avatar-icon { width: 20px; height: 20px; border-radius: 50%; background: #c9d3da; overflow: hidden; position: relative; }
  .avatar-icon::before { content: ""; position: absolute; width: 8px; height: 8px; border-radius: 50%; background: #fff; left: 6px; top: 3px; }
  .avatar-icon::after { content: ""; position: absolute; width: 14px; height: 10px; border-radius: 7px 7px 0 0; background: #fff; left: 3px; top: 12px; }

  .tabs { position: absolute; top: 78px; left: 12px; right: 12px; display: flex; justify-content: space-between; font-size: 9.5px; color: var(--text-dim); border-bottom: 1px solid var(--card-line); padding-bottom: 7px; }
  .tabs__item--active { color: var(--text); font-weight: 600; position: relative; }
  .tabs__item--active::after { content: ""; position: absolute; left: 12px; width: 15px; height: 2px; background: #fff; bottom: -8px; }

  .topic { position: absolute; left: 12px; width: 178px; height: 63px; border: 1px solid var(--card-line); border-radius: 2px; background: var(--card-bg); }
  .topic__icon { position: absolute; left: 8px; top: 11px; width: 41px; height: 41px; border-radius: 50%; background: var(--icon-bg); border: 2px solid rgba(255,255,255,0.5); display: flex; align-items: center; justify-content: center; }
  .topic__title { position: absolute; left: 56px; top: 8px; font-size: 11px; font-weight: 600; }
  .topic__text { position: absolute; left: 56px; top: 28px; font-size: 7.6px; line-height: 11px; color: var(--text-soft); width: 118px; }

  .portrait { position: absolute; left: 52px; top: 72px; width: 98px; height: 98px; border-radius: 50%; padding: 4px; }
  .portrait--gold { background: linear-gradient(135deg, #fff2a0, var(--gold) 50%, #b8860b); }
  .portrait--silver { background: linear-gradient(135deg, #ffffff, var(--silver) 50%, #8e979e); }
  .portrait--bronze { background: linear-gradient(135deg, #f5c27e, var(--bronze) 50%, #8a4d14); }
  .portrait__photo { width: 100%; height: 100%; border-radius: 50%; background: radial-gradient(circle at 40% 35%, #8c8c8c, #3a3a3a 60%, #1c1c1c); }
  .profile__name { position: absolute; top: 175px; width: 100%; text-align: center; font-size: 11.5px; font-weight: 600; }
  .profile__role { position: absolute; top: 190px; width: 100%; text-align: center; font-size: 8.5px; color: var(--text-soft); }
  .divider { position: absolute; left: 12px; right: 12px; top: 212px; height: 1px; background: var(--card-line); }
  .section-title { position: absolute; left: 12px; font-size: 11px; font-weight: 600; }
  .gear { position: absolute; left: 12px; top: 241px; width: 166px; height: 82px; border: 1px solid var(--card-line); background: var(--card-bg); }
  .gear--peek { left: 191px; width: 20px; top: 246px; height: 72px; }
  .gear__photo { position: absolute; left: 8px; top: 8px; width: 58px; height: 65px; background: radial-gradient(ellipse at 50% 55%, #5e6246 0%, #6e7255 40%, #f4f4f0 72%); }
  .gear__title { position: absolute; left: 73px; top: 5px; font-size: 10.5px; font-weight: 600; }
  .gear__set { position: absolute; left: 73px; top: 21px; font-size: 7.5px; color: var(--text-dim); }
  .gear__date { position: absolute; left: 70px; top: 48px; font-size: 6.8px; font-weight: 700; }
  .awards { position: absolute; top: 356px; left: 0; width: 100%; }
  .award { position: absolute; width: 56px; text-align: center; }
  .award svg { display: block; margin: 0 auto; }
  .award__label { font-size: 9px; font-weight: 600; margin-top: 4px; }
  .award--common { left: 17px; } .award--rare { left: 73px; } .award--epic { left: 129px; }
  .award--rare .award__label { color: var(--rare); }
  .award--epic .award__label { color: var(--epic); }
  .btn-mates { position: absolute; left: 46px; top: 407px; width: 111px; height: 23px; border: 1px solid var(--accent); border-radius: 2px; background: var(--button-bg); color: var(--accent); font-size: 8.5px; font-weight: 600; display: flex; align-items: center; justify-content: center; }

  .mate { position: absolute; left: 13px; width: 178px; height: 63px; border: 1px solid var(--card-line); background: var(--card-bg); }
  .mate__avatar { position: absolute; left: 8px; top: 10px; width: 42px; height: 42px; border-radius: 50%; padding: 2.5px; }
  .mate__avatar--gold { background: linear-gradient(135deg, #fff0a0, var(--gold), #b8860b); }
  .mate__avatar--silver { background: linear-gradient(135deg, #fff, var(--silver), #8e979e); }
  .mate__avatar--bronze { background: linear-gradient(135deg, #f5c27e, var(--bronze), #8a4d14); }
  .mate__photo { width: 100%; height: 100%; border-radius: 50%; background: radial-gradient(circle at 50% 45%, #c89a80, #6a5448 60%, #3c3a38); }
  .mate__name { position: absolute; left: 56px; top: 9px; font-size: 11px; font-weight: 600; }
  .mate__role { position: absolute; left: 56px; top: 31px; font-size: 8.5px; color: var(--text-soft); }
  .mate__status { position: absolute; left: 56px; top: 43px; font-size: 8.5px; color: var(--text-soft); }
  .mate__status b { color: var(--text); }
  .header-line { position: absolute; left: 12px; right: 12px; top: 73px; height: 1px; background: var(--card-line); }
</style>
</head>
<body>

<!-- Screen 1: topic list -->
<section class="screen" style="left:73px">
  <div class="screen__bar"></div>
  <header class="header">
    <div class="brand"><span class="brand__mark"></span><span class="brand__name">Torvu</span></div>
    <span class="header__login">Login</span><span class="avatar-icon"></span>
  </header>
  <nav class="tabs">
    <span class="tabs__item tabs__item--active">Common</span><span>Rare</span><span>Epic</span><span>Upcoming</span>
  </nav>
  <article class="topic" style="top:113px">
    <div class="topic__icon" role="img" aria-label="Wolf emblem"></div>
    <h3 class="topic__title">Wolf</h3>
    <p class="topic__text">Lorem Ipsum is simply dummy text of the printing and type.</p>
  </article>
  <article class="topic" style="top:189px">
    <div class="topic__icon">
      <svg width="20" height="18" viewBox="0 0 20 18" fill="none" stroke="#fff" stroke-width="1.3"><path d="M1 3l6-2 6 2 6-2v14l-6 2-6-2-6 2z"/><path d="M7 1v14M13 3v14M1 9h18"/></svg>
    </div>
    <h3 class="topic__title">Karte</h3>
    <p class="topic__text">Lorem Ipsum is simply dummy text of the printing and type.</p>
  </article>
  <article class="topic" style="top:265px">
    <div class="topic__icon">
      <svg width="20" height="20" viewBox="0 0 20 20" stroke="#fff" stroke-width="2" stroke-linecap="round"><path d="M3 3l14 14M17 3L3 17"/><path d="M2 14l4 4M18 14l-4 4" stroke-width="1.5"/></svg>
    </div>
    <h3 class="topic__title">Kampf</h3>
    <p class="topic__text">Lorem Ipsum is simply dummy text of the printing and type.</p>
  </article>
  <article class="topic" style="top:341px">
    <div class="topic__icon">
      <svg width="20" height="20" viewBox="0 0 20 20" fill="#fff"><path d="M18 2c-5 0-9 3-11 8l3 3c5-2 8-6 8-11z"/><path d="M6 9l-4 1 3 2zM11 14l-1 4-2-3z"/><circle cx="13" cy="7" r="1.5" fill="#173346"/><path d="M4 14l-2 4 4-2z"/></svg>
    </div>
    <h3 class="topic__title">Rakete</h3>
    <p class="topic__text">Lorem Ipsum is simply dummy text of the printing and type.</p>
  </article>
</section>

<!-- Screens 2–4: player cards -->
<section class="screen" style="left:286px">
  <div class="screen__bar"></div>
  <div class="screen__backdrop" role="img" aria-label="Faded player photo backdrop"></div>
  <header class="header">
    <div class="brand"><span class="brand__mark"></span><span class="brand__name">Torvu</span></div>
    <span class="header__login header__login--bold">Login</span><span class="avatar-icon"></span>
  </header>
  <div class="portrait portrait--gold"><div class="portrait__photo" role="img" aria-label="Player portrait photo"></div></div>
  <h2 class="profile__name">Myface</h2>
  <p class="profile__role">Warrier in traing</p>
  <div class="divider"></div>
  <h3 class="section-title" style="top:220px">Equipment</h3>
  <article class="gear">
    <div class="gear__photo" role="img" aria-label="Olive hooded jacket product photo"></div>
    <h4 class="gear__title">The wolf</h4>
    <p class="gear__set">Set : Lorem Ipsum text</p>
    <p class="gear__date">Equipped : 26 March 2019</p>
  </article>
  <div class="gear gear--peek"></div>
  <h3 class="section-title" style="top:332px">Achievements</h3>
  <div class="awards">
    <div class="award award--common"><svg width="22" height="30" viewBox="0 0 22 30"><path d="M5 16l-3 12 5-3 2 4 3-11zM17 16l3 12-5-3-2 4-3-11z" fill="#dfe4e8"/><circle cx="11" cy="11" r="10" fill="#dfe4e8"/><circle cx="11" cy="11" r="7.5" fill="#fff" stroke="#1b3444" stroke-width="1"/><text x="11" y="14.5" font-size="9" font-weight="700" text-anchor="middle" fill="#1b3444" font-family="Open Sans, sans-serif">10</text></svg><p class="award__label">Common</p></div>
    <div class="award award--rare"><svg width="22" height="30" viewBox="0 0 22 30"><path d="M5 16l-3 12 5-3 2 4 3-11zM17 16l3 12-5-3-2 4-3-11z" fill="#f0883a"/><circle cx="11" cy="11" r="10" fill="#f0883a"/><circle cx="11" cy="11" r="7.5" fill="#fff" stroke="#1b3444" stroke-width="1"/><text x="11" y="14.5" font-size="9" font-weight="700" text-anchor="middle" fill="#1b3444" font-family="Open Sans, sans-serif">5</text></svg><p class="award__label">Rare</p></div>
    <div class="award award--epic"><svg width="22" height="30" viewBox="0 0 22 30"><path d="M5 16l-3 12 5-3 2 4 3-11zM17 16l3 12-5-3-2 4-3-11z" fill="#f4c21f"/><circle cx="11" cy="11" r="10" fill="#f4c21f"/><circle cx="11" cy="11" r="7.5" fill="#fff" stroke="#1b3444" stroke-width="1"/><text x="11" y="14.5" font-size="9" font-weight="700" text-anchor="middle" fill="#1b3444" font-family="Open Sans, sans-serif">3</text></svg><p class="award__label">Epic</p></div>
  </div>
  <div class="btn-mates">ADD MATES</div>
</section>

<section class="screen" style="left:499px">
  <div class="screen__bar"></div>
  <div class="screen__backdrop" role="img" aria-label="Faded player photo backdrop"></div>
  <header class="header">
    <div class="brand"><span class="brand__mark"></span><span class="brand__name">Torvu</span></div>
    <span class="header__login">Login</span><span class="avatar-icon"></span>
  </header>
  <div class="portrait portrait--silver"><div class="portrait__photo" role="img" aria-label="Player portrait photo"></div></div>
  <h2 class="profile__name">Myface</h2>
  <p class="profile__role">Warrier in traing</p>
  <div class="divider"></div>
  <h3 class="section-title" style="top:220px">Equipment</h3>
  <article class="gear">
    <div class="gear__photo" role="img" aria-label="Olive hooded jacket product photo"></div>
    <h4 class="gear__title">The wolf</h4>
    <p class="gear__set">Set : Lorem Ipsum text</p>
    <p class="gear__date">Equipped : 26 March 2019</p>
  </article>
  <div class="gear gear--peek"></div>
  <h3 class="section-title" style="top:332px">Achievements</h3>
  <div class="awards">
    <div class="award award--common"><svg width="22" height="30" viewBox="0 0 22 30"><path d="M5 16l-3 12 5-3 2 4 3-11zM17 16l3 12-5-3-2 4-3-11z" fill="#dfe4e8"/><circle cx="11" cy="11" r="10" fill="#dfe4e8"/><circle cx="11" cy="11" r="7.5" fill="#fff" stroke="#1b3444" stroke-width="1"/><text x="11" y="14.5" font-size="9" font-weight="700" text-anchor="middle" fill="#1b3444" font-family="Open Sans, sans-serif">10</text></svg><p class="award__label">Common</p></div>
    <div class="award award--rare"><svg width="22" height="30" viewBox="0 0 22 30"><path d="M5 16l-3 12 5-3 2 4 3-11zM17 16l3 12-5-3-2 4-3-11z" fill="#f0883a"/><circle cx="11" cy="11" r="10" fill="#f0883a"/><circle cx="11" cy="11" r="7.5" fill="#fff" stroke="#1b3444" stroke-width="1"/><text x="11" y="14.5" font-size="9" font-weight="700" text-anchor="middle" fill="#1b3444" font-family="Open Sans, sans-serif">5</text></svg><p class="award__label">Rare</p></div>
    <div class="award award--epic"><svg width="22" height="30" viewBox="0 0 22 30"><path d="M5 16l-3 12 5-3 2 4 3-11zM17 16l3 12-5-3-2 4-3-11z" fill="#f4c21f"/><circle cx="11" cy="11" r="10" fill="#f4c21f"/><circle cx="11" cy="11" r="7.5" fill="#fff" stroke="#1b3444" stroke-width="1"/><text x="11" y="14.5" font-size="9" font-weight="700" text-anchor="middle" fill="#1b3444" font-family="Open Sans, sans-serif">3</text></svg><p class="award__label">Epic</p></div>
  </div>
  <div class="btn-mates">ADD MATES</div>
</section>

<section class="screen" style="left:712px">
  <div class="screen__bar"></div>
  <div class="screen__backdrop" role="img" aria-label="Faded player photo backdrop"></div>
  <header class="header">
    <div class="brand"><span class="brand__mark"></span><span class="brand__name">Torvu</span></div>
    <span class="header__login header__login--bold">Login</span><span class="avatar-icon"></span>
  </header>
  <div class="portrait portrait--bronze"><div class="portrait__photo" role="img" aria-label="Player portrait photo"></div></div>
  <h2 class="profile__name">Myface</h2>
  <p class="profile__role">Warrier in traing</p>
  <div class="divider"></div>
  <h3 class="section-title" style="top:220px">Equipment</h3>
  <article class="gear">
    <div class="gear__photo" role="img" aria-label="Olive hooded jacket product photo"></div>
    <h4 class="gear__title">The wolf</h4>
    <p class="gear__set">Set : Lorem Ipsum text</p>
    <p class="gear__date">Equipped : 26 March 2019</p>
  </article>
  <div class="gear gear--peek"></div>
  <h3 class="section-title" style="top:332px">Achievements</h3>
  <div class="awards">
    <div class="award award--common"><svg width="22" height="30" viewBox="0 0 22 30"><path d="M5 16l-3 12 5-3 2 4 3-11zM17 16l3 12-5-3-2 4-3-11z" fill="#dfe4e8"/><circle cx="11" cy="11" r="10" fill="#dfe4e8"/><circle cx="11" cy="11" r="7.5" fill="#fff" stroke="#1b3444" stroke-width="1"/><text x="11" y="14.5" font-size="9" font-weight="700" text-anchor="middle" fill="#1b3444" font-family="Open Sans, sans-serif">10</text></svg><p class="award__label">Common</p></div>
    <div class="award award--rare"><svg width="22" height="30" viewBox="0 0 22 30"><path d="M5 16l-3 12 5-3 2 4 3-11zM17 16l3 12-5-3-2 4-3-11z" fill="#f0883a"/><circle cx="11" cy="11" r="10" fill="#f0883a"/><circle cx="11" cy="11" r="7.5" fill="#fff" stroke="#1b3444" stroke-width="1"/><text x="11" y="14.5" font-size="9" font-weight="700" text-anchor="middle" fill="#1b3444" font-family="Open Sans, sans-serif">5</text></svg><p class="award__label">Rare</p></div>
    <div class="award award--epic"><svg width="22" height="30" viewBox="0 0 22 30"><path d="M5 16l-3 12 5-3 2 4 3-11zM17 16l3 12-5-3-2 4-3-11z" fill="#f4c21f"/><circle cx="11" cy="11" r="10" fill="#f4c21f"/><circle cx="11" cy="11" r="7.5" fill="#fff" stroke="#1b3444" stroke-width="1"/><text x="11" y="14.5" font-size="9" font-weight="700" text-anchor="middle" fill="#1b3444" font-family="Open Sans, sans-serif">3</text></svg><p class="award__label">Epic</p></div>
  </div>
  <div class="btn-mates">ADD MATES</div>
</section>

<!-- Screen 5: mates list -->
<section class="screen" style="left:925px">
  <div class="screen__bar"></div>
  <header class="header">
    <div class="brand"><span class="brand__mark"></span><span class="brand__name">Torvu</span></div>
    <span class="header__login header__login--bold">User Name</span><span class="avatar-icon"></span>
  </header>
  <div class="header-line"></div>
  <article class="mate" style="top:86px">
    <div class="mate__avatar mate__avatar--silver"><div class="mate__photo" role="img" aria-label="Mate profile photo"></div></div>
    <h3 class="mate__name">Myface</h3><p class="mate__role">Warrior in training</p><p class="mate__status">Status : <b>Silver</b></p>
  </article>
  <article class="mate" style="top:158px">
    <div class="mate__avatar mate__avatar--gold"><div class="mate__photo" role="img" aria-label="Mate profile photo"></div></div>
    <h3 class="mate__name">Myface</h3><p class="mate__role">Warrior in training</p><p class="mate__status">Status : <b>Gold</b></p>
  </article>
  <article class="mate" style="top:229px">
    <div class="mate__avatar mate__avatar--bronze"><div class="mate__photo" role="img" aria-label="Mate profile photo"></div></div>
    <h3 class="mate__name">Myface</h3><p class="mate__role">Warrior in training</p><p class="mate__status">Status : <b>Silver</b></p>
  </article>
  <article class="mate" style="top:301px">
    <div class="mate__avatar mate__avatar--gold"><div class="mate__photo" role="img" aria-label="Mate profile photo"></div></div>
    <h3 class="mate__name">Myface</h3><p class="mate__role">Warrior in training</p><p class="mate__status">Status : <b>Gold</b></p>
  </article>
  <article class="mate" style="top:372px">
    <div class="mate__avatar mate__avatar--gold"><div class="mate__photo" role="img" aria-label="Mate profile photo"></div></div>
    <h3 class="mate__name">Myface</h3><p class="mate__role">Warrior in training</p><p class="mate__status">Status : <b>Gold</b></p>
  </article>
</section>

</body>
</html>
```